website refresh/redesign needed for Printing e commerce website

We'd like a website refresh/redesign done with the specific goal of having the site act as a more effective funnel for leads.<br/><br/>We think that the current design is outdated.<br/><br/>We want our customers and partners to still recognize the website, Is a big chunk of our business is repeat orders. <br/>so it should not be a full redesign. General color scheme and such should remain the same so that it is clear we are the same company. <br/><br/>However, the updated website design should look more polished and convey high-quality products and services that we provide. <br/><br/>Our website is https://shopledgerformsnet.quillpaperdepot.com/ if you want to take a look at our current website design. <br/><br/>we need 3 pages redesigned... <br/><br/>1. homepage:https://shopledgerformsnet.quillpaperdepot.com/<br/><br/>2. Category page: <br/>https://shopledgerformsnet.quillpaperdepot.com/order-computer-checks-c-4.html<br/><br/>3. Product detail page: https://shopledgerformsnet.quillpaperdepot.com/voucher-computer-checks-p-35.html<br/><br/> I can provide many more pictures of our products if needed.<br/><br/><br/>BTW. I have another project here on brief bazaar, you can check the other ones too, so to make it easier to do both when working on this.<br/><br/> Please reach out to me should you have any questions or comments.

```html
<!DOCTYPE html>
<html lang="en">
<head>
<meta charset="utf-8">
<title>Ledger Forms Shop</title>
<link rel="stylesheet" href="https://fonts.googleapis.com/css2?family=Montserrat:wght@600;700&family=Nunito:wght@400&family=Arimo:ital@0;1&display=swap">
<style>
:root{
  --ink:#1f1f1f;
  --green:#8ee57a;
  --dark-green:#1e3d12;
  --star:#f0a00c;
  --muted:#8a8a8a;
  --faq-text:#555555;
  --panel:#ffffff;
  --check:#e4e6fb;
  --check-line:#4c4fd6;
  --shadow:0 10px 28px rgba(0,0,0,.10);
}
*{box-sizing:border-box;margin:0;padding:0}
html,body{width:773px;height:1200px;overflow:hidden;background:#f3f3f3}
.page{position:relative;width:755px;height:1200px;background:#fff;margin-left:9px;font-family:"Arimo",sans-serif;color:var(--ink)}
.abs{position:absolute}
.nav{top:14px;left:0;width:755px;height:20px}
.nav .links{position:absolute;left:162px;top:3px;display:flex;gap:25px;font-family:"Nunito",sans-serif;font-size:7.5px;color:#222}
.stars{display:flex;gap:1px;align-items:center}
.stars svg{fill:var(--star)}
.quote-pill{left:178px;top:77px;width:396px;height:33px;border-radius:18px;background:#fff;box-shadow:var(--shadow)}
.top-stars{left:345px;top:73px;z-index:2}
.quote-text{left:178px;top:91px;width:396px;text-align:center;font-style:italic;font-size:7px}
.author{font-family:"Nunito",sans-serif;font-size:7px;color:var(--muted);white-space:nowrap}
.hero{left:111px;top:180px;width:520px;height:125px;border-radius:62px;background:#fff;box-shadow:var(--shadow)}
.brand{left:172px;top:222px;display:flex;align-items:center;gap:10px;font-family:"Montserrat",sans-serif;font-weight:700;font-size:31px;color:var(--ink)}
.brand .mark{width:26px;height:26px;border-radius:50%;background:var(--green)}
.cat{width:140px;text-align:center;font-family:"Montserrat",sans-serif;font-weight:700;font-size:12px}
.cat .thumb{width:70px;height:70px;border-radius:50%;margin:0 auto 10px;box-shadow:var(--shadow)}
.panel{background:var(--panel);border-radius:60px;box-shadow:var(--shadow)}
.panel-title{font-family:"Montserrat",sans-serif;font-weight:700;font-size:11.5px;text-align:center;letter-spacing:.2px}
.more{font-family:"Montserrat",sans-serif;font-weight:700;font-size:12px;text-align:center}
.grid{left:130px;top:580px;display:grid;grid-template-columns:repeat(6,70px);column-gap:14.5px;row-gap:18px}
.product{width:70px;height:70px;background:linear-gradient(135deg,#eef0ff,var(--check));border:1px solid var(--check-line);border-left:22px solid #f6f6fd}
.reviews{left:96px;top:883px;display:flex;flex-direction:column}
.review{display:flex;gap:6px;width:240px}
.review .who{width:56px;flex:none;display:flex;flex-direction:column;align-items:center;gap:1px}
.review p{font-style:italic;font-size:7px;line-height:1.2;padding-top:3px;width:166px}
.faq{left:425px;top:876px;width:250px}
.faq li{list-style:none;display:flex;gap:12px;align-items:center;font-size:7.5px;color:var(--faq-text);line-height:1.3;margin-bottom:12.5px}
.faq li::before{content:"";flex:none;width:6px;height:6px;border-radius:50%;background:var(--dark-green)}
</style>
</head>
<body>
<svg width="0" height="0" style="position:absolute"><defs><symbol id="star" viewBox="0 0 10 10"><path d="M5 0l1.5 3.4 3.5.3-2.7 2.3.8 3.6L5 7.8 1.9 9.6l.8-3.6L0 3.7l3.5-.3z"/></symbol></defs></svg>
<div class="page">
  <header class="abs nav">
    <svg class="abs" style="left:21px;top:0" width="11" height="13" viewBox="0 0 11 13"><circle cx="5.5" cy="3.3" r="3.2" fill="var(--dark-green)"/><path d="M0 13c0-4 2.3-6 5.5-6S11 9 11 13z" fill="var(--dark-green)"/></svg>
    <nav class="links"><span>Business Checks</span><span>Computer Checks</span><span>TallyDesk Check</span><span>Accessories</span><span>Help</span><span>Re-Order</span></nav>
    <svg class="abs" style="left:582px;top:4px" width="10" height="11" viewBox="0 0 10 11"><circle cx="4" cy="4" r="3.3" fill="none" stroke="#333" stroke-width=".9"/><path d="M6.4 6.6 9.4 10.4" stroke="#333" stroke-width=".9"/></svg>
    <svg class="abs" style="left:722px;top:0" width="16" height="14" viewBox="0 0 16 14"><path d="M1 5h12l-2 6H3z" fill="var(--dark-green)"/><path d="M4 5 7 1l3 4" fill="none" stroke="var(--dark-green)" stroke-width="1"/><circle cx="12" cy="11" r="2.8" fill="#fff" stroke="var(--dark-green)" stroke-width=".8"/><text x="12" y="12.6" font-size="4" text-anchor="middle" fill="var(--dark-green)">5</text></svg>
  </header>

  <div class="abs quote-pill"></div>
  <div class="abs stars top-stars">
    <svg width="7" height="7"><use href="#star"/></svg><svg width="9" height="9"><use href="#star"/></svg><svg width="11" height="11"><use href="#star"/></svg><svg width="9" height="9"><use href="#star"/></svg><svg width="7" height="7"><use href="#star"/></svg>
  </div>
  <p class="abs quote-text">These people at ledger forms shop are Super. Best Services. Fast Delivery. Will defiantly order again here!</p>
  <span class="abs author" style="left:527px;top:112px">Marla | Deal, NJ</span>

  <div class="abs hero"></div>
  <div class="abs brand"><span class="mark"></span>Ledger Forms Shop</div>

  <div class="abs cat" style="left:85px;top:369px"><div class="thumb" role="img" aria-label="Stacked business check sheets" style="background:linear-gradient(135deg,#f2f3ff,#dfe2fb)"></div>Checks by Type</div>
  <div class="abs cat" style="left:310px;top:369px"><div class="thumb" role="img" aria-label="Check layout sample" style="background:linear-gradient(180deg,#d9e4ec,#b9cbd6)"></div>Checks by Layout</div>
  <div class="abs cat" style="left:535px;top:369px"><div class="thumb" style="background:#fff;display:flex;align-items:center;justify-content:center;font-family:'Montserrat',sans-serif;font-weight:700;font-size:10px;color:var(--ink)">TallyDesk</div>Checks by Software</div>

  <section class="abs panel" style="left:69px;top:518px;width:616px;height:280px">
    <h2 class="panel-title" style="margin-top:16px">ALL PRODUCTS</h2>
    <p class="abs more" style="left:0;right:0;top:262px">more</p>
  </section>
  <div class="abs grid">
    <div class="product" role="img" aria-label="Business check product"></div>
    <div class="product" role="img" aria-label="Business check product"></div>
    <div class="product" role="img" aria-label="Business check product"></div>
    <div class="product" role="img" aria-label="Business check product"></div>
    <div class="product" role="img" aria-label="Business check product"></div>
    <div class="product" role="img" aria-label="Business check product"></div>
    <div class="product" role="img" aria-label="Business check product"></div>
    <div class="product" role="img" aria-label="Business check product"></div>
    <div class="product" role="img" aria-label="Business check product"></div>
    <div class="product" role="img" aria-label="Business check product"></div>
    <div class="product" role="img" aria-label="Business check product"></div>
    <div class="product" role="img" aria-label="Business check product"></div>
  </div>

  <section class="abs panel" style="left:71px;top:825px;width:286px;height:278px">
    <h2 class="panel-title" style="margin-top:19px">REVIEWS</h2>
    <p class="abs more" style="left:0;right:0;top:259px">more</p>
  </section>
  <div class="abs reviews">
    <div class="review" style="height:56px"><div class="who"><div class="stars"><svg width="7" height="7"><use href="#star"/></svg><svg width="9" height="9"><use href="#star"/></svg><svg width="11" height="11"><use href="#star"/></svg><svg width="9" height="9"><use href="#star"/></svg><svg width="7" height="7"><use href="#star"/></svg></div><span class="author">Marla | Deal, NJ</span></div><p>These people at ledger forms shop are Super. Best Services. Fast Delivery. Will defiantly order again here!</p></div>
    <div class="review" style="height:54px"><div class="who"><div class="stars"><svg width="7" height="7"><use href="#star"/></svg><svg width="9" height="9"><use href="#star"/></svg><svg width="11" height="11"><use href="#star"/></svg><svg width="9" height="9"><use href="#star"/></svg><svg width="7" height="7"><use href="#star"/></svg></div><span class="author">Marla | Deal, NJ</span></div><p>These people at ledger forms shop are Super. Best Services. Fast Delivery. Will defiantly order again here!</p></div>
    <div class="review" style="height:27px"><div class="who"><div class="stars"><svg width="7" height="7"><use href="#star"/></svg><svg width="9" height="9"><use href="#star"/></svg><svg width="11" height="11"><use href="#star"/></svg><svg width="9" height="9"><use href="#star"/></svg><svg width="7" height="7"><use href="#star"/></svg></div><span class="author">Marla | Deal, NJ</span></div><p>These people at ledger forms shop are Super.</p></div>
    <div class="review" style="height:27px"><div class="who"><div class="stars"><svg width="7" height="7"><use href="#star"/></svg><svg width="9" height="9"><use href="#star"/></svg><svg width="11" height="11"><use href="#star"/></svg><svg width="9" height="9"><use href="#star"/></svg><svg width="7" height="7"><use href="#star"/></svg></div><span class="author">Marla | Deal, NJ</span></div><p>These people at ledger forms shop are Super.</p></div>
    <div class="review" style="height:27px"><div class="who"><div class="stars"><svg width="7" height="7"><use href="#star"/></svg><svg width="9" height="9"><use href="#star"/></svg><svg width="11" height="11"><use href="#star"/></svg><svg width="9" height="9"><use href="#star"/></svg><svg width="7" height="7"><use href="#star"/></svg></div><span class="author">Marla | Deal, NJ</span></div><p>These people at ledger forms shop are Super.</p></div>
  </div>

  <section class="abs panel" style="left:399px;top:825px;width:286px;height:278px">
    <h2 class="panel-title" style="margin-top:19px">FAQ’s</h2>
    <p class="abs more" style="left:0;right:0;top:259px">more</p>
  </section>
  <ul class="abs faq">
    <li>Lorem ipsum dolor sit amet, consectetur adipiscing elit, sed do eiusmod tempor incididunt ut labore et dolore magna aliqua.</li>
    <li>Lorem ipsum dolor sit amet, consectetur adipiscing elit, sed do eiusmod tempor incididunt ut labore et dolore magna aliqua.</li>
    <li style="margin-top:5px">Lorem ipsum dolor sit amet, consectetur adipiscing elit, sed do eiusmod tempor incididunt ut labore et dolore magna aliqua.</li>
    <li style="margin-top:3px">Lorem ipsum dolor sit amet, consectetur adipiscing elit, sed do eiusmod tempor incididunt ut labore et dolore magna aliqua.</li>
    <li>Lorem ipsum dolor sit amet, consectetur adipiscing elit, sed do eiusmod tempor incididunt ut labore et dolore magna aliqua.</li>
  </ul>
</div>
</body>
</html>
```